Crimson Ledger.com is wanting to create a Facebook Ad to attract buyers to come to their website. We are wanting buyers to register for free and create an account on Crimson Ledger. com. We want to increase the number of buyers by posting an ad on Facebook groups. The buyer will click the link to our websites registration page.
https://www.crimsonledger.com/account/users/register

Semi Trucks
Semi Trailers
Construction Equipment
Farm Equipment
Trailers
ATV/UTV
Boats
RVs

```html
<!DOCTYPE html>
<html lang="en">
<head>
<meta charset="utf-8">
<title>Crimson Ledger – Trusted Insurance Auction Site</title>
<link rel="stylesheet" href="https://fonts.googleapis.com/css2?family=Exo+2:ital,wght@1,800;1,900&family=Montserrat:wght@500;600;700;800&family=Oswald:wght@700&display=swap">
<style>
  :root{
    --white:#ffffff;
    --ink:#1c1c1c;
    --text:#2a2a2a;
    --muted:#5a5a5a;
    --red:#d8201c;
    --red-dark:#b5121b;
    --blue:#2f6fd6;
    --blue-dark:#1d4fa8;
    --pill:#e4e4e4;
    --band:#0d0d0d;
    --shape:#efefef;
    --shape-2:#e6e6e6;
  }
  *{margin:0;padding:0;box-sizing:border-box}
  html,body{width:1200px;height:1200px;overflow:hidden;background:var(--white)}
  .canvas{position:relative;width:1200px;height:1200px;overflow:hidden;background:var(--white);font-family:"Montserrat",sans-serif;color:var(--text)}
  .edge{position:absolute;top:0;bottom:0;width:12px;background:repeating-linear-gradient(135deg,#9a9a9a 0 2px,transparent 2px 7px)}
  .edge--left{left:0}
  .edge--right{right:0}
  .backdrop{position:absolute;inset:0}
  .fan{position:absolute;left:0;top:0;width:1200px;height:640px}
  .brand{position:absolute;left:0;right:0;top:112px;text-align:center;font-family:"Oswald",sans-serif;font-weight:700;color:var(--ink);font-size:78px;line-height:84px;letter-spacing:4px;text-transform:uppercase}
  .headline{position:absolute;left:0;right:0;top:652px;text-align:center;font-family:"Exo 2",sans-serif;font-style:italic;font-weight:900;font-size:55px;letter-spacing:1px;color:var(--red);text-shadow:2px 3px 0 #3a0b0b}
  .categories{position:absolute;left:37px;right:37px;top:720px;height:38px;display:flex;gap:4px;list-style:none}
  .categories li{background:var(--band);color:var(--white);font-family:"Exo 2",sans-serif;font-style:italic;font-weight:800;font-size:21px;line-height:34px;padding:0 7px;border-bottom:4px solid var(--red);box-shadow:0 4px 0 var(--blue);white-space:nowrap;flex:auto;text-align:left}
  .features{position:absolute;left:45px;top:776px;width:610px;list-style:none}
  .feature{position:relative;height:56px;margin-bottom:30px;display:flex;align-items:center}
  .feature__bar{position:absolute;left:20px;right:0;top:0;bottom:0;background:var(--pill);border-radius:28px 0 0 28px;clip-path:polygon(0 0,96% 0,100% 50%,96% 100%,0 100%)}
  .feature__icon{position:relative;width:54px;height:54px;border-radius:50%;background:var(--blue);display:flex;align-items:center;justify-content:center;z-index:1}
  .feature__text{position:relative;z-index:1;margin-left:16px;font-weight:600;font-size:18.5px;color:var(--ink)}
  .about{position:absolute;left:675px;top:788px;width:468px;font-size:19px;line-height:25.5px;color:var(--muted);text-align:justify;font-weight:500}
  .phone{position:absolute;left:695px;top:952px;display:flex;align-items:center;gap:14px}
  .phone__icon{width:46px;height:46px;border-radius:50%;background:var(--blue-dark);display:flex;align-items:center;justify-content:center}
  .phone__number{font-weight:700;font-size:51px;color:var(--ink);letter-spacing:1px}
  .cta{position:absolute;left:320px;top:1060px;width:560px;height:96px;border-radius:48px;background:var(--red-dark);color:var(--white);font-weight:700;font-size:48px;letter-spacing:1px;display:flex;align-items:center;justify-content:center;text-decoration:none}
  .url{position:absolute;left:0;right:0;top:1163px;text-align:center;font-weight:800;font-size:21px;color:var(--ink)}
</style>
</head>
<body>
<main class="canvas">
  <svg class="backdrop" width="1200" height="1200" aria-hidden="true">
    <polygon points="0,420 520,640 0,900" fill="var(--shape)"/>
    <polygon points="1200,380 700,700 1200,980" fill="var(--shape)"/>
    <polygon points="300,620 900,560 640,1000" fill="var(--shape-2)" opacity=".6"/>
    <polygon points="0,1000 380,880 200,1200 0,1200" fill="var(--shape)"/>
    <polygon points="1200,1000 860,1100 1200,1200" fill="var(--shape)"/>
  </svg>

  <div class="edge edge--left"></div>
  <div class="edge edge--right"></div>

  <svg class="fan" viewBox="0 0 1200 640" aria-hidden="false">
    <g stroke="var(--white)" stroke-width="8">
      <path role="img" aria-label="Photo of a yellow excavator on a dirt lot" fill="#8f8a5c" d="M412.9 167 L196.2 128.8 A410 410 0 0 0 264.1 435.2 L444.4 309 A190 190 0 0 1 412.9 167 Z"/>
      <path role="img" aria-label="Photo of a damaged dark blue semi truck cab" fill="#4a5566" d="M448.3 314.3 L272.6 446.7 A410 410 0 0 0 528.8 603.8 L567 387.1 A190 190 0 0 1 448.3 314.3 Z"/>
      <path role="img" aria-label="Photo of a green side-by-side UTV" fill="#5c6650" d="M573.6 388.2 L542.9 606 A410 410 0 0 0 740.2 585.3 L665 378.5 A190 190 0 0 1 573.6 388.2 Z"/>
      <path role="img" aria-label="Photo of a white long-nose semi truck" fill="#a9aeb3" d="M671.2 376.2 L753.6 580.2 A410 410 0 0 0 1003.8 128.8 L787.1 167 A190 190 0 0 1 671.2 376.2 Z"/>
    </g>
  </svg>

  <div class="brand">Crimson<br>Ledger</div>

  <h1 class="headline">TRUSTED INSURANCE AUCTION SITE</h1>

  <ul class="categories">
    <li>Semi trucks</li>
    <li>Semi Trailers</li>
    <li>Construction Equipment</li>
    <li>Farm Equipment</li>
    <li>Trailers</li>
    <li>ATV/UTV</li>
    <li>Boats</li>
    <li>RV</li>
  </ul>

  <ul class="features">
    <li class="feature">
      <span class="feature__bar"></span>
      <span class="feature__icon">
        <svg width="26" height="26" viewBox="0 0 24 24" fill="none" stroke="#fff" stroke-width="2"><path d="M7 4h10v5a5 5 0 0 1-10 0z"/><path d="M7 6H4a3 3 0 0 0 3 4M17 6h3a3 3 0 0 1-3 4M12 14v4M8 20h8"/></svg>
      </span>
      <span class="feature__text">Instant online salvage submissions 24 hours a day</span>
    </li>
    <li class="feature">
      <span class="feature__bar"></span>
      <span class="feature__icon">
        <svg width="26" height="26" viewBox="0 0 24 24" fill="none" stroke="#fff" stroke-width="2" stroke-linejoin="round"><path d="M21 3 3 11l7 3 3 7z"/><path d="M21 3 10 14"/></svg>
      </span>
      <span class="feature__text">Instant email alerts to buyers when new listings are posted</span>
    </li>
    <li class="feature">
      <span class="feature__bar"></span>
      <span class="feature__icon">
        <svg width="26" height="26" viewBox="0 0 24 24" fill="none" stroke="#fff" stroke-width="2"><path d="M3 17l5-6 4 4 6-8"/><circle cx="3" cy="17" r="1.6"/><circle cx="8" cy="11" r="1.6"/><circle cx="12" cy="15" r="1.6"/><circle cx="18" cy="7" r="1.6"/></svg>
      </span>
      <span class="feature__text">Friendly, professional staff</span>
    </li>
  </ul>

  <p class="about">We specialize in connecting verified buyers to certified sellers of wrecked or salvaged semi-trucks, trailers, equipment or other heavy duty specialty vehicles with insurance companies and certified sellers.</p>

  <div class="phone">
    <span class="phone__icon">
      <svg width="26" height="26" viewBox="0 0 24 24" fill="#fff"><path d="M6.6 10.8a15.1 15.1 0 0 0 6.6 6.6l2.2-2.2a1 1 0 0 1 1-.25 11.4 11.4 0 0 0 3.6.57 1 1 0 0 1 1 1V20a1 1 0 0 1-1 1A17 17 0 0 1 3 4a1 1 0 0 1 1-1h3.5a1 1 0 0 1 1 1c0 1.25.2 2.45.57 3.57a1 1 0 0 1-.25 1z"/></svg>
    </span>
    <span class="phone__number">(555) 214-3308</span>
  </div>

  <a class="cta" href="https://www.crimsonledger.com/account/users/register">REGISTER FREE</a>

  <p class="url">www.crimsonledger.com</p>
</main>
</body>
</html>
```